Business Card Design - Corporate

Create a sleek elegant business card layout while suggesting a color scheme. Convey cutting edge technology while maintaining a corporate feel that is easily readable.

Company designs and manufactures consumer electronic products for mass retail that are mainly app driven.

(vector logo and die-line provided)

Target Market(s)

Corporate level, tech industry.

Industry/Entity Type

Business

Contact Information for Business Card

Generic Info:

Name
Title
email
address
phone 1
phone 2
website (quillbarn.com) on back

Font styles to use
Sans Serif

Requirements
Must have
• At least 2 colors + white on one side.
Nice to have
• Solid suggestion on color for logo and overall design. Color flood on back of card.
Should not have
• background texture like... marble, stone, patterns or circuit boards

```html
<!DOCTYPE html>
<html lang="en">
<head>
<meta charset="utf-8">
<title>Quillbarn Business Card</title>
<link href="https://fonts.googleapis.com/css2?family=Roboto:wght@400;500&family=Montserrat:wght@500&display=swap" rel="stylesheet">
<style>
  :root {
    --page-bg: #d9dadc;
    --card-dark: #1f1f20;
    --card-light: #ffffff;
    --ink-white: #f4f4f4;
    --ink-dark: #4a4b4d;
    --accent-blue: #1b73c4;
  }
  * { margin: 0; padding: 0; box-sizing: border-box; }
  html, body { width: 1200px; height: 900px; overflow: hidden; }
  body {
    background: var(--page-bg);
    font-family: "Roboto", Arial, sans-serif;
    position: relative;
  }
  .card {
    position: absolute;
    left: 290px;
    width: 620px;
    height: 354px;
    border-radius: 26px;
    box-shadow: 0 10px 26px rgba(0,0,0,0.22);
  }
  .card-back { top: 58px; background: var(--card-light); }
  .card-front { top: 478px; background: var(--card-dark); }

  .wordmark {
    font-family: "Montserrat", Arial, sans-serif;
    font-weight: 500;
    letter-spacing: 0.16em;
    display: flex;
    align-items: center;
    gap: 10px;
  }
  .wordmark-dot {
    width: 12px; height: 12px; border-radius: 50%;
    background: var(--accent-blue);
  }

  .card-back .wordmark {
    position: absolute;
    top: 150px; left: 0; right: 0;
    justify-content: center;
    font-size: 36px;
    color: var(--ink-dark);
  }
  .back-website {
    position: absolute;
    bottom: 40px; left: 0; right: 0;
    text-align: center;
    font-size: 15px;
    color: var(--ink-dark);
    letter-spacing: 0.03em;
  }

  .front-content {
    position: absolute;
    left: 250px;
    top: 62px;
    color: var(--ink-white);
  }
  .card-front .wordmark {
    font-size: 40px;
    color: var(--ink-white);
    margin-bottom: 10px;
  }
  .person-name {
    font-size: 22px;
    font-weight: 500;
    letter-spacing: 0.14em;
    text-transform: uppercase;
  }
  .person-title {
    font-size: 17px;
    color: var(--accent-blue);
    letter-spacing: 0.08em;
    margin-bottom: 12px;
  }
  .address { font-size: 16px; line-height: 1.35; letter-spacing: 0.05em; margin-bottom: 6px; }
  .contact-list { list-style: none; font-size: 16px; letter-spacing: 0.05em; }
  .contact-list li { display: flex; align-items: center; gap: 10px; line-height: 1.45; }
  .contact-icon { width: 16px; height: 16px; fill: var(--accent-blue); flex-shrink: 0; }
</style>
</head>
<body>

<section class="card card-back" aria-label="Card back">
  <div class="wordmark">QUILLBARN<span class="wordmark-dot"></span></div>
  <p class="back-website">quillbarn.com</p>
</section>

<section class="card card-front" aria-label="Card front">
  <div class="front-content">
    <div class="wordmark">QUILLBARN<span class="wordmark-dot"></span></div>
    <p class="person-name">Owen Harlow</p>
    <p class="person-title">Managing Director</p>
    <p class="address">820 Alder Lane Suite 300<br>Millbrook, Il 60432</p>
    <ul class="contact-list">
      <li>
        <svg class="contact-icon" viewBox="0 0 16 16" aria-hidden="true"><path d="M3 1h10a1 1 0 0 1 1 1v12a1 1 0 0 1-1 1H3a1 1 0 0 1-1-1V2a1 1 0 0 1 1-1zm1 2v9h8V3zm4 10.2a.8.8 0 1 0 0 .01z"/></svg>
        0481-206-374
      </li>
      <li>
        <svg class="contact-icon" viewBox="0 0 16 16" aria-hidden="true"><path d="M3.6 1.5l2.2 2.7-1.3 1.6c.9 2 2.5 3.6 4.5 4.6l1.6-1.3 2.7 2.2-1.2 2.2C7 13.2 2.8 9 1.5 3.7z"/></svg>
        0712-449-503
      </li>
      <li>
        <svg class="contact-icon" viewBox="0 0 16 16" aria-hidden="true"><path d="M1 3h14v10H1zm1.5 1.2L8 8.4l5.5-4.2z"/></svg>
        owenharlow@mailbox.com
      </li>
    </ul>
  </div>
</section>

</body>
</html>
```